Need Amazing Website for Consulting Company

We need an amazing website design for a Human Resources Consulting Company. This will be geared towards a more professional crowd, but we don't want it to be overly corporate and stuffy: Just, clean and professional and amazing. Please use the video link below for further instruction.

http://clipvarn.example/t/kzQmPoLe7

Thank You.

PS Logo file has been attached.

Target Market(s)

The target marketing is small business owners who have employees. These owners cant afford an in-house HR person so they would hire this client to consult and do the work for them.

Industry/Entity Type

It Company

Font styles to use
Sans Serif

Requirements
Must have
• Please watch video:

Must have spot for video on homepage.
Nice to have
• Clean, professional, but not overly corporate, we want a personal and fun feel to this site a bit to separate them from all the other executive type sites. This site should have some LIFE to it and reflect a local brand that is doing great things.
Should not have
• Should not be just a corporate site, should not be overly stuffy, should not be overly boring.

```html
<!DOCTYPE html>
<html lang="en">
<head>
<meta charset="utf-8">
<title>Mesa Ridge HR Consulting</title>
<link rel="stylesheet" href="https://fonts.googleapis.com/css2?family=Arimo:wght@400;700&family=Open+Sans:wght@400;600;700&display=swap">
<style>
:root{
  --red:#c0162f;
  --red-dark:#a8122a;
  --black:#000;
  --white:#fff;
  --ink:#222;
  --muted:#555;
  --panel:#f7f7f7;
  --line:#dcdcdc;
  --footer-text:#cfcfcf;
  --icon-gray:#7a7a7a;
}
*{box-sizing:border-box;margin:0;padding:0}
html,body{width:1130px;height:1200px;overflow:hidden}
body{position:relative;background:var(--white);font-family:"Arimo",Arial,sans-serif;color:var(--ink)}
.abs{position:absolute}

/* top bar */
.topbar{left:0;top:0;width:1130px;height:25px;background:var(--red);color:var(--white);font-size:11px}
.share{left:131px;top:6px;display:flex;align-items:center;gap:4px}
.share .dot{width:15px;height:15px;border-radius:50%;background:var(--white)}
.share span{margin-right:4px}
.account{right:130px;top:6px}
.account a{color:var(--white);text-decoration:none}

/* header */
.brand{left:131px;top:50px;display:flex;align-items:center;gap:12px}
.brand-name{font-weight:700;font-size:24px;line-height:27px;color:var(--black)}
.brand-mark{width:22px;height:22px;border-radius:50%;background:var(--red)}
.search{left:712px;top:71px;width:288px;height:44px;border:1px solid #e3e3e3;background:var(--white)}
.search span{position:absolute;left:9px;top:14px;font-size:12px;color:#333}
.search-btn{position:absolute;right:-1px;top:-1px;width:40px;height:44px;background:var(--black)}

/* nav */
.mainnav{left:0;top:148px;width:1130px;height:42px;background:var(--black)}
.mainnav a{position:absolute;top:0;height:42px;line-height:42px;text-align:center;color:var(--white);font-size:13px;text-decoration:none;border-right:1px solid #444}
.mainnav a.active{background:var(--red);border-right:none}

/* hero */
.hero{left:0;top:190px;width:1130px;height:405px;background:linear-gradient(90deg,#dcdcdc 0%,#f3f3f3 20%,#c9c4be 45%,#b9b4ae 62%,#e9e9e9 85%,#f5f5f5 100%)}
.video{left:131px;top:248px;width:427px;height:308px;background:linear-gradient(#5a5a5a,#262626)}
.hero-title{left:701px;top:244px;color:var(--white);font-weight:700;font-size:29px;line-height:34px;text-shadow:0 1px 3px rgba(0,0,0,.35)}
.hero-list{left:713px;top:364px;list-style:none;color:var(--white);font-size:15.5px;text-shadow:0 1px 3px rgba(0,0,0,.4)}
.hero-list li{height:36px;display:flex;align-items:center;gap:10px}
.hero-list li::before{content:"";width:7px;height:7px;background:var(--red);border:2px solid var(--white)}
.btn{background:var(--red);color:var(--white);font-family:"Open Sans",Arial,sans-serif;font-weight:600;text-align:center;border-radius:2px}
.consult{left:773px;top:481px;width:149px;height:34px;line-height:34px;font-size:16px;border:1px solid var(--red-dark)}

/* content */
.content{left:0;top:595px;width:1130px;height:426px;background:var(--panel);border-top:12px solid var(--white)}
.divider{top:615px;width:1px;height:385px;background:var(--line)}
.col-title{top:628px;font-size:19px;color:var(--red);padding-bottom:9px;border-bottom:1px solid var(--line)}
.col-title b{font-weight:400;color:var(--ink)}
.welcome-photo{left:138px;top:685px;width:265px;height:145px;border-radius:3px;background:linear-gradient(135deg,#6b7a8c,#d9dde2 55%,#3a4250)}
.welcome-sub{left:139px;top:848px;color:var(--red);font-size:15px}
.welcome-text{left:138px;top:873px;width:270px;font-size:12.5px;line-height:16.5px;color:#222}
.readmore{left:217px;top:948px;width:84px;height:28px;line-height:28px;font-size:12.5px;font-family:"Arimo",Arial,sans-serif;font-weight:700}
.news-thumb{left:437px;width:74px;height:74px;border-radius:50%;background:radial-gradient(circle at 45% 40%,#eef1f4,#9aa6b3 70%,#5f6b78)}
.news-item{left:532px;width:170px;font-size:12px;line-height:15.5px;color:#222}
.news-item h3{font-weight:400;font-size:14.5px;color:var(--red);margin-bottom:4px}
.news-item .date{color:#555;font-size:11.5px;margin-bottom:2px}
.field{left:726px;width:270px;background:var(--white);border:1px solid #d6d6d6;border-radius:3px;font-family:"Open Sans",Arial,sans-serif;font-size:12.5px;font-weight:600;color:#333;padding:10px 10px}
.submit{left:817px;top:947px;width:82px;height:29px;line-height:29px;font-size:16px;font-weight:700}

/* footer */
.footer-rule{left:0;top:1021px;width:1130px;height:7px;background:var(--red)}
.footer{left:0;top:1028px;width:1130px;height:172px;background:var(--black)}
.f-title{top:1050px;color:var(--white);font-size:18.5px}
.f-list{list-style:none;color:var(--footer-text);font-size:12.5px;line-height:19.2px;top:1079px}
.f-contact{left:497px;top:1079px;color:var(--footer-text);font-size:12px}
.f-contact .name{font-weight:700;font-size:13px;margin-bottom:6px}
.f-row{display:flex;align-items:flex-start;gap:7px;margin-bottom:6px;line-height:14px}
.f-row svg{flex:none;margin-top:1px}
.social{left:684px;top:1083px;display:flex;gap:8px}
.social span{width:22px;height:22px;border-radius:50%;background:var(--icon-gray)}
.f-brand{left:858px;top:1048px;width:142px;height:100px;background:#1a1a1a;display:flex;align-items:center;justify-content:center;text-align:center;color:#555;font-weight:700;font-size:16px;line-height:19px}
.copyright{left:784px;top:1165px;color:var(--footer-text);font-size:10.5px}
</style>
</head>
<body>

<header>
  <div class="abs topbar">
    <div class="abs share"><span>SHARE</span><i class="dot"></i><i class="dot"></i><i class="dot"></i></div>
    <div class="abs account"><a href="#">LOG IN</a> &nbsp;|&nbsp; <a href="#">REGISTER</a> &nbsp;|&nbsp; <a href="#">CONTACTUS</a></div>
  </div>

  <div class="abs brand">
    <div class="brand-name">Mesa Ridge HR<br>Consulting</div>
    <i class="brand-mark"></i>
  </div>

  <div class="abs search">
    <span>Search</span>
    <div class="search-btn">
      <svg width="40" height="44" viewBox="0 0 40 44"><circle cx="18" cy="20" r="6" fill="none" stroke="#fff" stroke-width="2.5"/><line x1="22.5" y1="24.5" x2="27" y2="29" stroke="#fff" stroke-width="3" stroke-linecap="round"/></svg>
    </div>
  </div>

  <nav class="abs mainnav">
    <a class="active" href="#" style="left:131px;width:84px">HOME</a>
    <a href="#" style="left:215px;width:129px">ABOUT US</a>
    <a href="#" style="left:344px;width:153px">OUR&nbsp; SERVICES</a>
    <a href="#" style="left:497px;width:147px">LATEST&nbsp; NEWS</a>
    <a href="#" style="left:644px;width:132px">CONTACTUS</a>
    <a href="#" style="left:776px;width:143px">TESTIMONIAL</a>
    <a href="#" style="left:919px;width:81px;border-right:none">BLOG</a>
  </nav>
</header>

<section class="abs hero" role="img" aria-label="Blurred photo of colleagues talking in a bright office"></section>
<div class="abs video" aria-label="Video player">
  <svg class="abs" style="left:183px;top:124px" width="60" height="60" viewBox="0 0 60 60"><circle cx="30" cy="30" r="28" fill="#d31c2c"/><polygon points="23,17 23,43 44,30" fill="#fff"/></svg>
</div>
<h1 class="abs hero-title" style="font-weight:700">Lorem Ipsum<br>is simply dummy text<br>Lorem Ipsum</h1>
<ul class="abs hero-list">
  <li>Lorem Ipsum is simply dummy text</li>
  <li>Lorem Ipsum is simply dummy text</li>
  <li>Lorem Ipsum is simply dummy text</li>
</ul>
<div class="abs btn consult">Consult Now</div>

<main>
  <div class="abs content"></div>
  <div class="abs divider" style="left:420px"></div>
  <div class="abs divider" style="left:709px"></div>

  <h2 class="abs col-title" style="left:138px;width:265px">Welcome</h2>
  <div class="abs welcome-photo" role="img" aria-label="Photo of business people shaking hands at a meeting table"></div>
  <h3 class="abs welcome-sub" style="font-weight:400">Lorem Ipsum is simply dummy text</h3>
  <p class="abs welcome-text">Lorem Ipsum is simply dummy text of the printing and typesetting industry. Lorem Ipsum has been the industry's standard dummy text ever since the 1500s,</p>
  <div class="abs btn readmore">Read more</div>

  <h2 class="abs col-title" style="left:436px;width:256px"><b>Latest</b> News</h2>
  <div class="abs news-thumb" style="top:673px" role="img" aria-label="Photo of colleagues reviewing documents"></div>
  <div class="abs news-item" style="top:676px"><h3>Lorem Ipsum is simply</h3><div class="date">25-12-2013</div>Lorem Ipsum is simply dummy text of the printing</div>
  <div class="abs news-thumb" style="top:780px" role="img" aria-label="Photo of a presenter at a whiteboard"></div>
  <div class="abs news-item" style="top:782px"><h3>Lorem Ipsum is simply</h3><div class="date">13-1-2014</div>Lorem Ipsum is simply dummy text of the printing</div>
  <div class="abs news-thumb" style="top:886px" role="img" aria-label="Photo of a team meeting in an office"></div>
  <div class="abs news-item" style="top:888px"><h3>Lorem Ipsum is simply</h3><div class="date">22-2-2014</div>Lorem Ipsum is simply dummy text of the printing</div>

  <h2 class="abs col-title" style="left:726px;width:270px;border-bottom:none"><b>Contact</b> us</h2>
  <div class="abs field" style="top:684px;height:37px">Name :</div>
  <div class="abs field" style="top:728px;height:38px">Email :</div>
  <div class="abs field" style="top:773px;height:37px">Phone number :</div>
  <div class="abs field" style="top:817px;height:37px">Address :</div>
  <div class="abs field" style="top:862px;height:64px">Message :</div>
  <div class="abs btn submit">Submit</div>
</main>

<footer>
  <div class="abs footer-rule"></div>
  <div class="abs footer"></div>

  <h4 class="abs f-title" style="left:131px;font-weight:400">NAVIGATION</h4>
  <ul class="abs f-list" style="left:131px"><li>Home</li><li>Aboutus</li><li>Services</li><li>News</li><li>Contactus</li></ul>

  <h4 class="abs f-title" style="left:302px;font-weight:400">SERVICES</h4>
  <ul class="abs f-list" style="left:304px"><li>Lorem Ipsum is simply</li><li>Lorem Ipsum is</li><li>Lorem Ipsum is</li><li>Lorem Ipsum is</li><li>Lorem Ipsum is simply</li></ul>

  <h4 class="abs f-title" style="left:497px;font-weight:400">CONTACT US</h4>
  <div class="abs f-contact">
    <div class="name">Mesa Ridge HR</div>
    <div class="f-row"><svg width="15" height="13" viewBox="0 0 15 13"><path d="M1 4 Q7.5 -1 14 4 L12 6 L10 4.5 L5 4.5 L3 6 Z" fill="#aaa"/><rect x="3" y="6.5" width="9" height="6" rx="1" fill="#aaa"/></svg>555-014-0392</div>
    <div class="f-row"><svg width="12" height="16" viewBox="0 0 12 16"><path d="M6 0 A6 6 0 0 1 12 6 C12 10 6 16 6 16 C6 16 0 10 0 6 A6 6 0 0 1 6 0Z" fill="#aaa"/><circle cx="6" cy="6" r="2.2" fill="#000"/></svg>Lorem Ipsum is simply<br>dummy text</div>
    <div class="f-row"><svg width="12" height="9" viewBox="0 0 12 9"><rect width="12" height="9" fill="#aaa"/><polyline points="0,0 6,5 12,0" fill="none" stroke="#000" stroke-width="1.2"/></svg>info@mesaridgehr.example</div>
  </div>

  <h4 class="abs f-title" style="left:680px;font-weight:400">FOLLOW US</h4>
  <div class="abs social"><span></span><span></span><span></span></div>

  <div class="abs f-brand">Mesa Ridge HR<br>Consulting</div>
  <p class="abs copyright">copyright2014, MesaRidgeHRConsulting, LLC.</p>
</footer>

</body>
</html>
```